Redesign of Business Cards to Update them!

We want a full overhaul of our business cards! We have a design that is almost 5 years old and it needs to be updated to be current

Address is 457 Calloway Court Suite B San Bernardino CA 92408
PH: 9094417382
Tindlebox.com

Hours M-F 10AM-4PM
Sat and Sunday Closed

```html
<!DOCTYPE html>
<html lang="en">
<head>
<meta charset="utf-8">
<title>Tindlebox Business Card</title>
<link rel="stylesheet" href="https://fonts.googleapis.com/css2?family=Montserrat:wght@500;600;800&display=swap">
<style>
  :root {
    --page-bg: #c7c7c7;
    --card-white: #ffffff;
    --brand-red: #ed1c24;
    --panel-navy: #182833;
    --ink-black: #111111;
    --text-light: #ffffff;
    --art-red: #f20d0d;
  }
  * { box-sizing: border-box; margin: 0; padding: 0; }
  html, body {
    width: 1200px;
    height: 1200px;
    overflow: hidden;
    background: var(--page-bg);
    font-family: "Montserrat", sans-serif;
  }
  .business-card {
    position: absolute;
    left: 50px;
    top: 270px;
    width: 1100px;
    height: 660px;
    display: flex;
  }
  .brand-side {
    position: relative;
    width: 493px;
    height: 100%;
    background: var(--card-white);
  }
  .mascot-art {
    position: absolute;
    left: 61px;
    top: 211px;
    width: 341px;
    height: 147px;
    border-radius: 10px;
    background: linear-gradient(90deg, var(--art-red) 0%, #ff5a5a 50%, var(--art-red) 100%);
    opacity: 0.85;
  }
  .brand-name {
    position: absolute;
    left: 61px;
    top: 384px;
    width: 367px;
    font-weight: 800;
    font-size: 54px;
    line-height: 64px;
    color: var(--ink-black);
    letter-spacing: 0.5px;
  }
  .accent-band {
    width: 57px;
    height: 100%;
    background: var(--brand-red);
  }
  .contact-side {
    position: relative;
    flex: 1;
    height: 100%;
    background: var(--panel-navy);
    color: var(--text-light);
  }
  .icon {
    position: absolute;
    width: 34px;
    height: 34px;
    fill: var(--text-light);
  }
  .contact-text {
    position: absolute;
    left: 0;
    width: 100%;
    text-align: center;
    font-weight: 600;
    font-size: 25px;
    letter-spacing: 1px;
  }
  .address {
    left: 78px;
    width: auto;
    text-align: left;
    top: 105px;
    font-size: 24px;
    line-height: 31px;
  }
  .divider {
    position: absolute;
    left: 78px;
    top: 477px;
    width: 393px;
    height: 3px;
    background: var(--text-light);
  }
  .hours-block {
    position: absolute;
    top: 575px;
    width: 200px;
    text-align: center;
    font-weight: 500;
    font-size: 21px;
    line-height: 27px;
    letter-spacing: 1px;
  }
  .hours-weekday { left: 28px; }
  .hours-weekend { left: 304px; }
</style>
</head>
<body>
  <div class="business-card">
    <section class="brand-side">
      <div class="mascot-art" role="img" aria-label="Illustration of two cartoon mascots with phones, a frown turning to a smile, joined by an arrow"></div>
      <div class="brand-name">Tindlebox</div>
    </section>
    <div class="accent-band"></div>
    <section class="contact-side">
      <svg class="icon" style="left:258px;top:53px" viewBox="0 0 24 24" aria-hidden="true">
        <path d="M12 1a7 7 0 0 0-7 7c0 5 7 12 7 12s7-7 7-12a7 7 0 0 0-7-7zm0 9.5A2.5 2.5 0 1 1 12 5.5a2.5 2.5 0 0 1 0 5z"/>
        <path d="M6 19c-2 .6-3 1.4-3 2.3C3 22.8 7 24 12 24s9-1.2 9-2.7c0-.9-1-1.7-3-2.3l-1 1.3c1 .3 1.6.6 1.6 1 0 .6-3 1.3-6.6 1.3s-6.6-.7-6.6-1.3c0-.4.6-.7 1.6-1z"/>
      </svg>
      <div class="contact-text address">457 Calloway Court Suite B,<br>San Bernardino, CA 92408.</div>

      <svg class="icon" style="left:258px;top:210px" viewBox="0 0 24 24" aria-hidden="true">
        <path d="M6.6 10.8a15 15 0 0 0 6.6 6.6l2.2-2.2a1 1 0 0 1 1-.25 11.4 11.4 0 0 0 3.6.57 1 1 0 0 1 1 1V20a1 1 0 0 1-1 1A17 17 0 0 1 3 4a1 1 0 0 1 1-1h3.5a1 1 0 0 1 1 1c0 1.25.2 2.45.57 3.57a1 1 0 0 1-.25 1z"/>
      </svg>
      <div class="contact-text" style="top:262px">9094417382</div>

      <svg class="icon" style="left:258px;top:330px" viewBox="0 0 24 24" aria-hidden="true">
        <path d="M12 2a10 10 0 1 0 0 20 10 10 0 0 0 0-20zm7.9 9h-3.4a15 15 0 0 0-1.3-6.3A8 8 0 0 1 19.9 11zM12 4c.9 1.2 2.3 3.6 2.5 7h-5C9.7 7.6 11.1 5.2 12 4zM8.8 4.7A15 15 0 0 0 7.5 11H4.1a8 8 0 0 1 4.7-6.3zM4.1 13h3.4a15 15 0 0 0 1.3 6.3A8 8 0 0 1 4.1 13zM12 20c-.9-1.2-2.3-3.6-2.5-7h5c-.2 3.4-1.6 5.8-2.5 7zm3.2-.7a15 15 0 0 0 1.3-6.3h3.4a8 8 0 0 1-4.7 6.3z"/>
      </svg>
      <div class="contact-text" style="top:384px">tindlebox.com</div>

      <div class="divider"></div>

      <svg class="icon" style="left:111px;top:532px" viewBox="0 0 24 24" aria-hidden="true">
        <path d="M12 2a10 10 0 1 0 0 20 10 10 0 0 0 0-20zm3.3 14.7L11 12.4V6h2v5.6l3.7 3.7z"/>
      </svg>
      <div class="hours-block hours-weekday">M-F<br>10AM-4PM</div>

      <svg class="icon" style="left:387px;top:532px" viewBox="0 0 24 24" aria-hidden="true">
        <path d="M7 1h2v3H7zm8 0h2v3h-2zM4 3h2v2h2V3h8v2h2V3h2a1 1 0 0 1 1 1v17a1 1 0 0 1-1 1H4a1 1 0 0 1-1-1V4a1 1 0 0 1 1-1zm1 6v11h14V9zm2 2h2v2H7zm4 0h2v2h-2zm4 0h2v2h-2zm-8 4h2v2H7zm4 0h2v2h-2zm4 0h2v2h-2z"/>
      </svg>
      <div class="hours-block hours-weekend">Sat &amp; Sunday<br>Closed</div>
    </section>
  </div>
</body>
</html>
```